Unique business card design

We are looking for a design that reflects our unique social media and online marketing agency "Kestrel Media". We are a young agency with a focus on speakers, coaches and trainers. In other words, we support people who want to do good with their work and help other people live a happier, more successful and fulfilling life, reach as many people as possible with their work and thus have an influence. Our values are: sustainability, creating added value, individuality, proactivity. We want our clients to feel comfortable with us and that's why the relationship with them is very important to us. We want every customer to become a lifelong friend of the company. Most of our clients are premium coaches, meaning they are in the higher priced segment and expect seriousness, professionalism and quality. All of these things should reflect our business card as well. I look forward to feedback. Best regards, Tomas Wylander

```html
<!DOCTYPE html>
<html lang="en">
<head>
<meta charset="utf-8">
<title>Kestrel Media — Business Card</title>
<link rel="stylesheet" href="https://fonts.googleapis.com/css2?family=Roboto:wght@400;500&family=Roboto+Condensed:wght@500;700&display=swap">
<style>
  :root {
    --backdrop: #2b2b2d;
    --paper: #f1f1f1;
    --navy: #02003f;
    --brand-blue: #0070b9;
    --mark-blue: #1f3fa8;
    --white: #ffffff;
    --muted: #9a9aa6;
    --tagline: #3a3aa8;
  }
  * { margin: 0; padding: 0; box-sizing: border-box; }
  html, body { width: 1200px; height: 960px; overflow: hidden; }
  body {
    background: var(--backdrop);
    position: relative;
    font-family: "Roboto", Arial, sans-serif;
  }
  .card {
    position: absolute;
    width: 600px;
    height: 343px;
  }
  .card--front { left: 314px; top: 113px; background: var(--paper); }
  .card--back { left: 311px; top: 472px; background: var(--navy); }

  .brand {
    position: absolute;
    left: 0; right: 0;
    display: flex;
    flex-direction: column;
    align-items: center;
  }
  .brand__row { display: flex; align-items: center; gap: 12px; }
  .brand__square { width: 30px; height: 30px; }
  .brand__name {
    font-family: "Roboto", Arial, sans-serif;
    font-weight: 500;
    font-size: 38px;
    letter-spacing: -0.5px;
    line-height: 1;
  }
  .brand__tagline {
    margin-top: 12px;
    font-size: 14px;
    letter-spacing: 0.6px;
  }
  .card--front .brand { top: 88px; }
  .card--front .brand__square { background: var(--mark-blue); }
  .card--front .brand__name { color: var(--navy); }
  .card--front .brand__tagline { color: var(--tagline); }
  .card--back .brand { top: 130px; }
  .card--back .brand__square { background: var(--brand-blue); }
  .card--back .brand__name { color: var(--white); }
  .card--back .brand__tagline { color: var(--tagline); }

  .band {
    position: absolute;
    top: 214px;
    height: 113px;
    color: var(--white);
  }
  .band--identity {
    left: 0; width: 298px;
    background: var(--navy);
    text-align: right;
    padding: 12px 21px 0 0;
  }
  .band--contact {
    left: 302px; width: 298px;
    background: var(--brand-blue);
    padding: 9px 0 0 18px;
  }
  .holder__name {
    font-family: "Roboto Condensed", Arial, sans-serif;
    font-weight: 700;
    font-size: 22px;
    line-height: 24px;
  }
  .holder__role {
    font-family: "Roboto Condensed", Arial, sans-serif;
    font-weight: 500;
    font-size: 16px;
    line-height: 22px;
  }
  .holder__address {
    margin-top: 10px;
    font-size: 14.5px;
    line-height: 19px;
    font-style: normal;
  }
  .contact-list { list-style: none; }
  .contact-list li {
    display: flex;
    align-items: center;
    gap: 8px;
    font-size: 14.5px;
    line-height: 19.2px;
  }
  .contact-list svg { width: 14px; height: 14px; flex: none; fill: var(--white); }

  .social {
    position: absolute;
    top: 273px;
    left: 0; right: 0;
    display: flex;
    justify-content: center;
    gap: 3px;
  }
  .social__dot {
    width: 26px; height: 26px;
    border-radius: 50%;
    background: var(--muted);
  }
</style>
</head>
<body>

<section class="card card--front" aria-label="Business card front">
  <div class="brand">
    <div class="brand__row">
      <span class="brand__square"></span>
      <span class="brand__name">Kestrel Media</span>
    </div>
    <p class="brand__tagline">Online Marketing Services</p>
  </div>

  <div class="band band--identity">
    <p class="holder__name">TOMAS WYLANDER</p>
    <p class="holder__role">CEO/FOUNDER</p>
    <address class="holder__address">1420 Alder Crest Road<br>Juneau, Alaska 99801</address>
  </div>

  <div class="band band--contact">
    <ul class="contact-list">
      <li>
        <svg viewBox="0 0 16 16" aria-hidden="true"><path d="M3.5 1.5l2.3 0 1.2 3.2-1.6 1.1c.8 1.8 2 3 3.8 3.8l1.1-1.6 3.2 1.2v2.3c0 .9-.7 1.5-1.6 1.5C6.7 12.8 3.2 9.3 2 4.6 1.9 2.3 2.6 1.5 3.5 1.5z"/></svg>
        612 480 3317
      </li>
      <li>
        <svg viewBox="0 0 16 16" aria-hidden="true"><path d="M4.5 1h7v14h-7zM5.8 2.5v9.5h4.4V2.5z"/><circle cx="8" cy="13.4" r=".8"/></svg>
        612 905 2846
      </li>
      <li>
        <svg viewBox="0 0 16 16" aria-hidden="true"><path d="M4 1h8v4H4zM1 6h14v6h-2v3H3v-3H1zM4.5 10v3.5h7V10z"/></svg>
        612 730 1958
      </li>
      <li>
        <svg viewBox="0 0 16 16" aria-hidden="true"><path d="M1 4h14v9H1zM2.3 5l5.7 4 5.7-4z" fill-rule="evenodd"/></svg>
        tomas@kestrelmedia.net
      </li>
      <li>
        <svg viewBox="0 0 16 16" aria-hidden="true"><circle cx="8" cy="8" r="6.5"/><path d="M4 5.5l2 1 .5 2-1.5 1 .5 2.5M10 3.5l-.5 2 2 1.5 2-.5M9.5 10.5l1.5 1.5" stroke="#0070b9" stroke-width="1.1" fill="none"/></svg>
        www.kestrelmedia.net
      </li>
    </ul>
  </div>
</section>

<section class="card card--back" aria-label="Business card back">
  <div class="brand">
    <div class="brand__row">
      <span class="brand__square"></span>
      <span class="brand__name">Kestrel Media</span>
    </div>
    <p class="brand__tagline">Online Marketing Services</p>
  </div>
  <div class="social" aria-label="Social media profiles">
    <span class="social__dot"></span>
    <span class="social__dot"></span>
    <span class="social__dot"></span>
    <span class="social__dot"></span>
    <span class="social__dot"></span>
  </div>
</section>

</body>
</html>
```